Card design for Heating and Cooling company

this is for a heating and cooling company we recently updated our logo and need to update our cards. We attached our logo so you can incorporate it into the card. We specialize in residential and commercial furnace and air condition repairs. Have been in business since 2014.

Phone number 555.284.9137

We need the following phrases
:Repairs, Installations, and maintenance
:Quality work at reasonable prices
:residential/commercial
:Licensed &Insured
:Email Pinegrovehvac47@mailbox-example.com
Name: Teodor K (Ted)
Also on back side I would like my logo with wording :Thank you for your business and refferal

Industry/Entity Type

Hvac

Contact Information for Business Card

:residential/commercial
:Licensed & Insured
Name: Teodor K (Ted)
Number:555.284.9136

Requirements
Must have
• Blue and red colors
Nice to have
• Maybe a pic of a furnace or air conditioner

```html
<!DOCTYPE html>
<html lang="en">
<head>
<meta charset="utf-8">
<title>Pinegrove Heating &amp; Cooling – Business Card</title>
<link rel="stylesheet" href="https://fonts.googleapis.com/css2?family=Arimo:wght@400;700&display=swap">
<style>
  :root {
    --page: #ffffff;
    --card: #ffffff;
    --card-edge: #8a8a8a;
    --accent-orange: #e8541e;
    --contact-blue: #3b4aa0;
    --ink: #111111;
    --mark-blue: #2fa6e0;
  }
  html, body {
    margin: 0;
    padding: 0;
    width: 1200px;
    height: 339px;
    overflow: hidden;
    background: var(--page);
    font-family: "Arimo", Arial, sans-serif;
  }
  .sheet {
    position: relative;
    width: 1200px;
    height: 339px;
  }
  .card {
    position: absolute;
    top: 2px;
    height: 332px;
    background: var(--card);
    border: 1px solid var(--card-edge);
    box-sizing: border-box;
  }
  .card--front { left: 12px; width: 595px; }
  .card--back  { left: 616px; width: 582px; }

  .services {
    position: absolute;
    left: 22px;
    top: 30px;
    margin: 0;
    padding: 0;
    list-style: none;
    color: var(--accent-orange);
    font-size: 24px;
    line-height: 33.5px;
  }
  .contact {
    position: absolute;
    left: 22px;
    top: 202px;
    margin: 0;
    padding: 0;
    list-style: none;
    color: var(--contact-blue);
    font-size: 24px;
    line-height: 36px;
  }

  .brand {
    position: absolute;
    display: flex;
    align-items: center;
    gap: 8px;
    color: var(--ink);
    font-weight: 700;
    text-transform: uppercase;
    line-height: 1.05;
    text-align: center;
  }
  .brand__square {
    width: 18px;
    height: 18px;
    background: var(--mark-blue);
    flex: none;
  }
  .brand__name { display: block; }
  .brand--front {
    left: 345px;
    top: 155px;
    font-size: 20px;
  }
  .brand--back {
    left: 50%;
    top: 130px;
    transform: translateX(-50%);
    font-size: 24px;
  }

  .thanks {
    position: absolute;
    left: 0;
    right: 0;
    top: 285px;
    margin: 0;
    text-align: center;
    color: var(--ink);
    font-weight: 700;
    font-size: 23px;
  }
</style>
</head>
<body>
<main class="sheet">
  <section class="card card--front" aria-label="Card front">
    <ul class="services">
      <li>Repairs, Installations and maintenance</li>
      <li>Quality work at reasonable prices</li>
      <li>Residential/commercial</li>
      <li>Licensed &amp; Insured</li>
    </ul>

    <div class="brand brand--front">
      <span class="brand__square" aria-hidden="true"></span>
      <span class="brand__name">Pinegrove<br>Heating &amp; Cooling</span>
    </div>

    <ul class="contact">
      <li>Name: Teodor K (Ted)</li>
      <li>Number: 555.284.9137</li>
      <li>Email: Pinegrovehvac47@mailbox-example.com</li>
    </ul>
  </section>

  <section class="card card--back" aria-label="Card back">
    <div class="brand brand--back">
      <span class="brand__square" aria-hidden="true"></span>
      <span class="brand__name">Pinegrove<br>Heating &amp; Cooling</span>
    </div>
    <p class="thanks">Thank you for your business and refferal</p>
  </section>
</main>
</body>
</html>
```